Stonewell Holdings

Professional looking business card using darker colours
I do not yet have a logo for the company so feel free to suggest
The business is based on consultancy and project management
Based in Melbourne
Business card can omit the word "Holdings" and can be Stonewell consulting etc.

Contact Name on card : Ravi Pelunkoda Contact number : +61433 512 604 Email address will be confirmed shortly.

```html
<!DOCTYPE html>
<html lang="en">
<head>
<meta charset="utf-8">
<title>Ravi Pelunkoda — Project Management Consultant</title>
<link rel="stylesheet" href="https://fonts.googleapis.com/css2?family=Cinzel:wght@700&family=Comfortaa:wght@400&family=Montserrat:wght@800&display=swap">
<style>
  :root {
    --card-dark: #1b2427;
    --card-mid: #1f2a2d;
    --card-dark-edge: #121a1c;
    --gold: #9c7e35;
    --sky: #27a9e1;
  }
  html, body {
    margin: 0;
    padding: 0;
    overflow: hidden;
    background: var(--card-dark-edge);
  }
  .card {
    position: relative;
    width: 1200px;
    height: 694px;
    overflow: hidden;
  }
  .card-surface {
    position: absolute;
    inset: 0;
    background: linear-gradient(180deg, var(--card-dark) 0%, var(--card-mid) 45%, var(--card-dark) 100%);
  }
  .brand {
    position: absolute;
    right: 48px;
    top: 150px;
    display: flex;
    align-items: center;
    gap: 16px;
    color: var(--sky);
  }
  .brand-mark {
    width: 40px;
    height: 40px;
    background: var(--sky);
  }
  .brand-name {
    margin: 0;
    font-family: "Montserrat", "Arial", sans-serif;
    font-weight: 800;
    font-size: 36px;
    line-height: 1;
    letter-spacing: 1px;
    white-space: nowrap;
  }
  .contact {
    position: absolute;
    left: 58px;
    top: 250px;
    width: 636px;
    text-align: center;
  }
  .contact-name {
    margin: 0 -10px 0 0;
    font-family: "Cinzel", "Times New Roman", serif;
    font-weight: 700;
    font-size: 54px;
    line-height: 1;
    letter-spacing: 9.5px;
    color: var(--gold);
    white-space: nowrap;
  }
  .contact-phone {
    margin: 14px -9px 0 0;
    font-family: "Cinzel", "Times New Roman", serif;
    font-weight: 700;
    font-size: 38px;
    line-height: 1;
    letter-spacing: 9px;
    color: var(--sky);
    white-space: nowrap;
  }
  .role {
    position: absolute;
    left: 690px;
    top: 558px;
    color: var(--sky);
  }
  .role-field {
    margin: 0;
    font-family: "Comfortaa", "Helvetica", sans-serif;
    font-weight: 400;
    font-size: 35px;
    line-height: 1;
    letter-spacing: 0.3px;
    white-space: nowrap;
  }
  .role-title {
    margin: 6px 0 0;
    font-family: "Montserrat", "Arial", sans-serif;
    font-weight: 800;
    font-size: 53px;
    line-height: 1;
    letter-spacing: 1px;
    white-space: nowrap;
  }
  .underline-bar {
    position: absolute;
    left: 0;
    top: 631px;
    width: 661px;
    height: 13px;
    background: var(--sky);
  }
</style>
</head>
<body>
  <main class="card">
    <div class="card-surface" role="img" aria-label="Dark charcoal wood grain background"></div>

    <div class="brand">
      <span class="brand-mark"></span>
      <p class="brand-name">Stonewell</p>
    </div>

    <section class="contact">
      <h1 class="contact-name">RAVI PELUNKODA</h1>
      <p class="contact-phone">+61433 512 604</p>
    </section>

    <section class="role">
      <p class="role-field">project management</p>
      <p class="role-title">CONSULTANT</p>
    </section>

    <div class="underline-bar"></div>
  </main>
</body>
</html>
```